Design Project - Finance Website (Only need PSD)

UPDATED PROJECT (Now only PSD needed)
Need a Pressbase design for a company called "Harrowgate Capital Finance". The company provides finance for corporate clients, businesses and property developers. The design should be business like with appealing colours that communicate trust. I have uploaded a banner and logo to be incorporated or feel free to design something better if you think you can.
** I now only need the PSD
** I want something that is actually designed rather than from a template.
Thanks
Updates
The website will be used for lead generation so the contact form with adjustable fields in the Pressbase backend should be fairly prominent on the page.
I have uploaded a banner and logo for the site. None of the designs I have seen so far were good enough so the first decent design using the new banner and logo provided will win the job. I do not want just a template that has been cut and paste from somewhere else, I want decent design. If anyone provides a decent design then I will give an extra bonus of $150.
Reason: I have uploaded a banner and logo for the site. None of the designs I have seen so far were good enough so the first decent design using the new banner and logo provided will win the job. I do not want just a template that has been cut and paste from somewhere else, I want decent design. If anyone provides a decent design then I will give an extra bonus of $150.
Thanks
Target Market(s)
Business owners & property developers
Industry/Entity Type
Finance
Requirements
Must have
- Contact form on home page that can be altered through the back end eg. ability to add or remove fields. Widgetised sidebars.
Nice to have
- Widgetised footer.

```html
<!DOCTYPE html>
<html lang="en">
<head>
<meta charset="utf-8">
<title>Harrowgate Capital Finance</title>
<link href="https://fonts.googleapis.com/css2?family=Source+Sans+3:wght@400;600;700&family=Arimo:wght@400;700&display=swap" rel="stylesheet">
<style>
  :root{
    --navy:#0b3a94;
    --navy-deep:#04163f;
    --blue:#1a4fb0;
    --red:#d81c1c;
    --red-dark:#a80f0f;
    --page:#ffffff;
    --canvas:#e6e6e6;
    --card:#dcdcdc;
    --text:#4a4a4a;
    --muted:#6b6b6b;
    --rule:#cfcfcf;
  }
  *{box-sizing:border-box;margin:0;padding:0}
  html,body{width:912px;height:1200px;overflow:hidden}
  body{background:var(--canvas);font-family:"Source Sans 3",sans-serif;color:var(--text);position:relative}
  .abs{position:absolute}

  .masthead{left:0;top:0;width:912px;height:146px;background:linear-gradient(180deg,#020a22 0%,#0a2a6e 60%,#1d4fb8 100%)}
  .masthead-edge{left:0;top:143px;width:912px;height:3px;background:#2a66d4}
  .brand{left:137px;top:0;width:79px;height:88px;background:#fff;border-radius:0 0 10px 10px;display:flex;align-items:center;justify-content:center;text-align:center;padding:6px}
  .brand span{font-size:12px;font-weight:700;color:var(--red);line-height:1.05}
  .account{left:642px;top:2px;width:147px;height:28px;background:var(--red);border:2px solid #e8e8e8;border-radius:2px;display:flex;color:#fff;font-size:11px;font-weight:600}
  .account a{flex:1;display:flex;align-items:center;justify-content:center;gap:6px;color:#fff;text-decoration:none}
  .account a+a{border-left:1px solid #f27c7c}

  .nav{left:123px;top:128px;height:18px;display:flex}
  .nav a{font-size:8px;color:#888;background:#dedede;padding:0 8px;line-height:18px;text-decoration:none;border-right:1px solid #c9c9c9}
  .nav a.current{background:#fff;color:var(--navy);font-weight:700}
  .search{left:642px;top:128px;width:148px;height:18px;background:#fff;font-size:9px;color:#888;padding-left:7px;line-height:18px}

  .page{left:107px;top:146px;width:697px;height:962px;background:var(--page)}

  .hero{left:122px;top:157px;width:668px;height:242px;background:var(--navy);border:1px solid var(--navy)}
  .lead-form{left:122px;top:157px;width:184px;height:194px}
  .field{position:absolute;left:4px;width:177px;height:61px;background:#fff;border:1px solid #c8d3ec}
  .field label{position:absolute;left:49px;top:-1px;width:82px;height:18px;background:var(--navy);color:#fff;font-size:11px;font-weight:600;text-align:center;line-height:18px;border-radius:0 0 4px 4px}
  .field .input{position:absolute;left:18px;top:27px;width:141px;height:21px;border:1px solid #b9b9b9;box-shadow:inset 0 1px 2px rgba(0,0,0,.15);background:#fff}
  .slide{left:308px;top:158px;width:481px;height:193px;background:#fff}
  .slide-kicker{left:322px;top:208px;font-size:11px;color:var(--navy);letter-spacing:-.4px}
  .slide-title{left:316px;top:240px;font-size:19px;line-height:22px;color:var(--navy);letter-spacing:-.8px;width:210px}
  .slide-title b{font-weight:700}
  .slide-sub{left:316px;top:290px;font-size:14px;color:var(--navy);letter-spacing:-.6px}
  .slide-photo{left:494px;top:186px;width:290px;height:142px;background:radial-gradient(ellipse at 55% 55%,#e7b58e 0%,#c98f66 35%,#f5ede4 75%,#ffffff 100%)}
  .slide-dots{left:754px;top:331px;display:flex;gap:3px}
  .slide-dots i{width:11px;height:11px;background:var(--blue);display:block;border-radius:2px}
  .send{left:170px;top:360px;width:91px;height:28px;background:linear-gradient(#f04040,var(--red-dark));border:2px solid #e6e6e6;color:#fff;font-size:10px;font-weight:600;display:flex;align-items:center;justify-content:center;gap:18px;box-shadow:0 1px 3px rgba(0,0,0,.4)}
  .hero-line{left:337px;top:364px;font-size:14px;color:#fff;letter-spacing:-.6px}
  .hero-line b{font-weight:700}
  .hero-cta{left:629px;top:362px;font-size:16px;font-weight:700;color:#fff;display:flex;align-items:center;gap:8px}
  .hero-cta i{width:23px;height:22px;background:var(--red);border:2px solid #fff;border-radius:3px;display:flex;align-items:center;justify-content:center}
  .hero-shadow{left:122px;top:399px;width:668px;height:14px;background:radial-gradient(ellipse at 50% 0,rgba(0,0,0,.22),transparent 70%)}

  .offer{top:421px;width:215px;height:211px;background:var(--card);border-radius:0 0 5px 5px}
  .offer-tab{position:absolute;left:0;top:0;width:107px;height:22px;background:var(--blue);color:#fff;font-size:11px;font-weight:600;padding-left:8px;line-height:22px;border-radius:3px 3px 0 0}
  .offer-tab-line{position:absolute;left:0;top:20px;width:215px;height:2px;background:var(--blue)}
  .offer-media{position:absolute;left:0;top:22px;width:215px;height:87px;background:#fff;border-radius:0 0 8px 0;overflow:hidden}
  .offer-photo{position:absolute;right:0;top:0;width:122px;height:87px}
  .offer-rate{position:absolute;left:7px;top:29px;color:var(--navy)}
  .offer-rate .intro{font-size:13px;display:block;line-height:14px}
  .offer-rate .row{display:flex;align-items:flex-start}
  .offer-rate .upto{font-size:7px;font-weight:700;margin:2px 3px 0 0}
  .offer-rate .num{font-size:44px;font-weight:700;letter-spacing:-1.5px;line-height:38px}
  .offer-rate .unit{font-size:16px;line-height:14px;margin:2px 0 0 1px}
  .offer-rate .unit small{display:block;font-size:7px;line-height:8px}
  .offer p{position:absolute;left:7px;font-family:Arimo,sans-serif;font-size:10px;line-height:12.8px;color:#333;width:204px}
  .offer .apply{position:absolute;right:10px;top:183px;height:18px;padding:0 6px;background:var(--red);border:1px solid #fff;outline:1px solid var(--red);color:#fff;font-family:Arimo,sans-serif;font-size:8px;font-weight:700;display:flex;align-items:center;gap:4px}

  .section-shadow{left:122px;top:640px;width:668px;height:10px;background:radial-gradient(ellipse at 50% 0,rgba(0,0,0,.15),transparent 70%)}

  .sidebar{left:137px;width:150px;list-style:none}
  .sidebar li{font-size:8px;line-height:16.6px;color:#777;padding-left:8px;position:relative}
  .sidebar li::before{content:"";position:absolute;left:0;top:7px;width:3px;height:3px;border-radius:50%;background:var(--blue)}
  .column-rule{left:295px;top:649px;width:1px;height:450px;background:var(--rule)}

  .article{left:308px;top:657px;width:484px;font-size:9.2px;line-height:12.1px;color:#555}
  .article h2{font-size:12.5px;font-weight:700;color:var(--navy);margin:14px 0 13px;letter-spacing:.1px}
  .article h3{font-size:9.5px;font-weight:700;color:var(--navy);margin:13px 0 11px}
  .article p.fine{font-size:7.4px;line-height:10px;color:#777}

  .footer{left:107px;top:1108px;width:697px;height:92px;background:var(--navy);color:#fff;font-family:Arimo,sans-serif;font-size:8px}
  .footer .credit{position:absolute;left:10px;top:7px}
  .footer .links{position:absolute;right:10px;top:7px;display:flex;gap:22px}
  .footer .copy{position:absolute;left:0;width:100%;top:69px;text-align:center}
</style>
</head>
<body>

<div class="abs masthead" role="img" aria-label="Night city skyline with lit office towers in deep blue"></div>
<div class="abs masthead-edge"></div>
<div class="abs brand"><span>Harrowgate Capital Finance</span></div>
<div class="abs account">
  <a href="#"><svg width="5" height="7" viewBox="0 0 5 7"><path d="M5 0L0 3.5 5 7z" fill="#fff"/></svg>SIGNUP</a>
  <a href="#">LOGIN<svg width="5" height="7" viewBox="0 0 5 7"><path d="M0 0L5 3.5 0 7z" fill="#fff"/></svg></a>
</div>
<nav class="abs nav">
  <a href="#">About Us</a><a href="#">Contact us</a><a href="#" class="current">Mezzanine Finance</a><a href="#">Privacy Policy</a><a href="#">Terms and Conditions</a>
</nav>
<div class="abs search">Type to search, then press enter</div>

<div class="abs page"></div>

<section class="abs hero"></section>
<form class="abs lead-form">
  <div class="field" style="top:3px"><label>Your Name</label><div class="input"></div></div>
  <div class="field" style="top:67px"><label>Your Number</label><div class="input"></div></div>
  <div class="field" style="top:132px"><label>Your Company</label><div class="input"></div></div>
</form>
<div class="abs slide"></div>
<div class="abs slide-kicker">Mezzanine Finance</div>
<svg class="abs" style="left:320px;top:222px" width="95" height="10" viewBox="0 0 95 10"><path d="M2 8 Q45 -2 92 3" stroke="#d81c1c" stroke-width="1.4" fill="none"/></svg>
<div class="abs slide-title"><b>Compare</b> several capital provider rates</div>
<div class="abs slide-sub"><b>Optimise</b> your capital returns</div>
<div class="abs slide-photo" role="img" aria-label="Photo of two business people shaking hands"></div>
<div class="abs slide-dots"><i></i><i></i></div>
<div class="abs send">SEND <svg width="5" height="7" viewBox="0 0 5 7"><path d="M0 0L5 3.5 0 7z" fill="#fff"/></svg></div>
<div class="abs hero-line">Access to real estate and <b>hedge funds</b></div>
<div class="abs hero-cta">Look &amp; Apply <i><svg width="8" height="10" viewBox="0 0 8 10"><path d="M0 0L8 5 0 10z" fill="#fff"/></svg></i></div>
<div class="abs hero-shadow"></div>

<article class="abs offer" style="left:129px">
  <div class="offer-tab-line"></div><div class="offer-tab">LOANS</div>
  <div class="offer-media">
    <div class="offer-photo" role="img" aria-label="Photo of hands holding a small model house" style="background:linear-gradient(120deg,#f2e8dc,#b8a58c 45%,#a3442c 80%,#6e2c1c)"></div>
    <div class="offer-rate"><span class="intro">Just</span><div class="row"><span class="num">6.3</span><span class="unit">%<small>APR<br>Representative</small></span></div></div>
  </div>
  <p style="top:114px">Whatever you're planning, you could make it happen with a great low rate. 6.3% APR Representative.</p>
  <p style="top:158px">For main ClearPath Account customers.</p>
  <div class="apply"><svg width="4" height="6" viewBox="0 0 4 6"><path d="M0 0L4 3 0 6z" fill="#fff"/></svg>Look &amp; Apply</div>
</article>

<article class="abs offer" style="left:349px">
  <div class="offer-tab-line"></div><div class="offer-tab">ONLINE ISA</div>
  <div class="offer-media">
    <div class="offer-photo" role="img" aria-label="Photo of a smiling woman" style="background:linear-gradient(120deg,#f6ede4,#e4b990 45%,#8a4a2a 80%,#2a3a7a)"></div>
    <div class="offer-rate"><span class="intro">Transfer to a great rate</span><div class="row"><span class="upto">Up to</span><span class="num">3.10</span><span class="unit">%<small>APR<br>Representative</small></span></div></div>
  </div>
  <p style="top:114px">Whatever you're planning, you could make it happen with a great low rate. 6.3% APR Representative.</p>
  <p style="top:158px">For main ClearPath Account customers.</p>
  <div class="apply"><svg width="4" height="6" viewBox="0 0 4 6"><path d="M0 0L4 3 0 6z" fill="#fff"/></svg>Look &amp; Apply</div>
</article>

<article class="abs offer" style="left:569px">
  <div class="offer-tab-line"></div><div class="offer-tab">CREADIT CARD</div>
  <div class="offer-media" style="border-radius:0 0 8px 8px">
    <div class="offer-photo" role="img" aria-label="Photo of a hand holding a silver card" style="background:linear-gradient(120deg,#ffffff,#c9ced6 45%,#6d7a96 75%,#0b2a6e)"></div>
    <div class="offer-rate"><span class="intro">Just</span><div class="row"><span class="num">6.3</span><span class="unit">%<small>APR<br>Representative</small></span></div></div>
  </div>
  <p style="top:114px">Whatever you're planning, you could make it happen with a great low rate. 6.3% APR Representative.</p>
  <p style="top:158px">For main ClearPath Account customers.</p>
  <div class="apply"><svg width="4" height="6" viewBox="0 0 4 6"><path d="M0 0L4 3 0 6z" fill="#fff"/></svg>Look &amp; Apply</div>
</article>

<div class="abs section-shadow"></div>

<ul class="abs sidebar" style="top:651px">
  <li>Mezzanine Debt UK</li><li>Mezzanine Debt Financing</li><li>Mezzanine Finance UK</li><li>Mezzanine Finance 2012</li><li>Providers</li><li>Mezzanine Funding</li><li>Mezzanine Financing Rates</li><li>Mezzanine Property Finance</li>
</ul>
<ul class="abs sidebar" style="top:800px">
  <li>Mezzanine Debt UK</li><li>Mezzanine Debt Financing</li><li>Mezzanine Finance UK</li><li>Mezzanine Finance 2012</li><li>Choosing Between Mezzanine Finance</li><li>Providers</li><li>Mezzanine Funding</li><li>Mezzanine Financing Rates</li><li>Mezzanine Property Finance</li>
</ul>
<ul class="abs sidebar" style="top:965px">
  <li>Mezzanine Debt UK</li><li>Mezzanine Debt Financing</li><li>Mezzanine Finance UK</li><li>Mezzanine Finance 2012</li>
</ul>
<div class="abs column-rule"></div>

<main class="abs article">
  <p>Mezzanine finance is a method of raising capital that is financed by debt. It fills the gap in a company's finance structure between equity and senior debt. This means that mezzanine financing has priority over the company's equity but is subordinate to the debts of senior lenders. A mezzanine debt may have several specific structures such as a convertible preferred debt, private securities and second-lien debt.</p>
  <h2>MEZZANINE FINANCE BENEFITS</h2>
  <p>A company must have a positive cash flow to use mezzanine financing. It is typically used to expand the company through leveraged buyouts, recapitalization and acquisitions. The common feature of these types of mezzanine financing is that they offer a risk/return ratio that is lower than that of equity, but greater than that of debt. Borrowers usually consider mezzanine financing after a senior lender is no longer willing to make additional loans. However, the company's financial structure must still have the capacity for additional long-term loans. Mezzanine financing is often combined with senior debt to reduce the amount of equity that the borrowing company must give to the lender.</p>
  <h2>MEZZANINE FINANCE USES</h2>
  <p>A company may use mezzanine finance for a variety of specific purposes. This includes growth opportunities such as the expansion of a plant, a new distribution channel, a new product or the acquisition of a property. The managers of a company may also use this type of financing to buy out the owners of the company as part of a succession or exit strategy. The capital provided by mezzanine financing in these scenarios is typically a small portion of the total capital available to the company. However, mezzanine financing is essential for corporate expansion and succession planning.</p>
  <h2>MEZZANINE FUNDING GAP</h2>
  <p>The funding gap between equity and senior debt is the primary reason for using mezzanine funding. This gap often occurs when accountants reduce the estimated value of a company's fixed assets, anticipating that the value of these assets will not be realized. Senior lenders may also be reluctant to use intangible assets as collateral, or they may wish to limit the company's risk from a particular source of income. The finance structure of some companies may also make the cost of equity prohibitively expensive.</p>
  <h3>LENDERS</h3>
  <p class="fine">Senior lenders typically view mezzanine financing as borrowing equity, although mezzanine financing has several advantages over equity. Mezzanine financing has greater security since it takes precedence over equity in the finance structure. Borrowing additional equity also reduces the value of the existing shares of stock. The dilution of stock from mezzanine financing is limited, since most of the loan is made through interest payments.</p>
</main>

<footer class="abs footer">
  <div class="credit">Powered by Fieldstone, the drag and drop Pressbase theme</div>
  <div class="links"><span>Administration Login</span><span>Go To Top</span></div>
  <div class="copy">Copyright © 2012 Harrowgate Capital Finance</div>
</footer>

</body>
</html>
```